Brochure and Logo design for nature connection support service

Brochure design for business supporting people with psycho-social disabilities to develop a connection with nature. We do bush walking, camping and bush-craft related activities to help people feel home in the outdoors. My vision is for more people to develop a transformative relationship with Nature creating more fulfilling, connected, and environmentally-sustainable communities. I have attached for inclusion some notes and a photo of myself.

I also need a logo. I have attached a sketch of a basic idea that I had incorporating a tree surrounding a sitting figure. The person, fire and tree could blend into each other and re-combine like an ouroborus (see attached image). I have also attached a circular image of thessaly sitting which has nice proportions for a circular logo.

For inspo, some concepts that I resonate with are: mind, consciousness, psychedelic values, wonder, wisdom, philosophy, plants, ecology, ecosystems (esp. Australian woodlands), the night sky, ancient civilisations, primitive societies, minimalism, balance, dynamic equilibrium...

Target Market(s)

The brochure will be aimed at potential participants, so should be concise and appealing. It will also be directed to the carers and Support Coordinators of people with disabilities, so it should be professional, sincere, and not sales-pitchy.

Logo Text

"nature connection" "support services" Some combinations of symbols and text and symbol without text

Requirements
Must have
• 1 page double sided able to be folded in three.
Green colour scheme
Photo of myself should be associated with the "contact" section. Can be cropped to headshot if appropriate etc. Neither photo should be too prominent. Other images are okay.

```html
<!DOCTYPE html>
<html lang="en">
<head>
<meta charset="utf-8">
<title>Wildroot Support Services – Brochure Inside</title>
<link rel="stylesheet" href="https://fonts.googleapis.com/css2?family=Roboto:ital,wght@0,400;0,500;0,700;0,900;1,400&display=swap">
<style>
  :root {
    --leaf: #67b847;
    --leaf-deep: #3f8f3e;
    --forest: #16793f;
    --ink: #1b1b1b;
    --white: #ffffff;
    --sun-start: #f26a2a;
    --sun-end: #f9b233;
    --sky: #9fd8f2;
    --lake: #0e3c5c;
  }
  * { margin: 0; padding: 0; box-sizing: border-box; }
  html, body { width: 1200px; height: 849px; overflow: hidden; background: var(--white); }
  body { font-family: "Roboto", sans-serif; color: var(--ink); }

  .brochure { position: relative; width: 1200px; height: 849px; overflow: hidden; }
  .panel { position: absolute; top: 0; width: 400px; height: 849px; }
  .panel--info { left: 0; background: var(--white); }
  .panel--contact { left: 400px; background: linear-gradient(180deg, var(--leaf) 0%, #56a443 55%, var(--leaf-deep) 100%); color: var(--white); }
  .panel--cover { left: 800px; background: var(--white); }

  .heading { position: absolute; left: 47px; line-height: 1; }
  .heading__lead { display: block; font-weight: 400; font-size: 26px; color: var(--leaf); }
  .heading__main { display: block; font-weight: 900; font-size: 37px; color: var(--leaf); margin-top: 3px; letter-spacing: -0.3px; }
  .heading__rule { position: absolute; height: 5px; right: 0; background: linear-gradient(90deg, var(--sun-start), var(--sun-end)); }

  .copy { position: absolute; left: 45px; width: 330px; font-size: 15.6px; line-height: 18.8px; }
  .copy p + p { margin-top: 18.8px; }
  .copy .note { font-style: italic; color: var(--leaf); }

  .panel--contact .heading { left: 49px; }
  .panel--contact .heading__lead, .panel--contact .heading__main { color: var(--white); }

  .portrait { position: absolute; left: 445px; top: 182px; width: 152px; height: 152px; border-radius: 50%; background: rgba(255,255,255,0.35); }
  .portrait__photo { position: absolute; left: 8px; top: 8px; width: 136px; height: 136px; border-radius: 50%; border: 3px solid var(--white); background: radial-gradient(circle at 50% 35%, #e9d2bf 0%, #b88c6e 40%, #2a2a26 75%); }

  .contact { position: absolute; left: 453px; width: 303px; }
  .contact__name { top: 345px; font-weight: 700; font-size: 18px; padding-bottom: 10px; border-bottom: 1.5px solid var(--white); }
  .contact__details { top: 389px; font-size: 17px; font-weight: 500; line-height: 21px; }
  .contact__bio { top: 458px; font-size: 15.6px; line-height: 18.8px; color: #eaf5df; }

  .scene { position: absolute; display: block; }
</style>
</head>
<body>
<main class="brochure">

  <section class="panel panel--info">
    <h2 class="heading" style="top:78px; width:353px;">
      <span class="heading__lead">What will</span>
      <span class="heading__main">I need?</span>
      <span class="heading__rule" style="left:130px; bottom:6px;"></span>
    </h2>
    <div class="copy" style="top:157px;">
      <p>All necessary equipment will be provided. Participants just need to wear clothes suitable for the outdoors and the current weather conditions. Non-essentials can safely be left behind.</p>
    </div>

    <h2 class="heading" style="top:357px; width:353px;">
      <span class="heading__lead">What does</span>
      <span class="heading__main">it cost?</span>
      <span class="heading__rule" style="left:130px; bottom:6px;"></span>
    </h2>
    <div class="copy" style="top:440px; width:335px;">
      <p>NDIS funded participants are billed under line item:<br>04_40x_0104_1_1 Assistance with social and community participation:<br>Access Community, Social and Recreational Activities - Level 2.</p>
      <p>For very high intensity supports, the Level 3 price limit may be applied with participant agreement.</p>
      <p class="note" style="margin-top:22px;">Transportation is included and can be billed as part of the support time.</p>
    </div>

    <svg class="scene" style="left:0; top:730px;" width="245" height="119" viewBox="0 0 245 119" role="img" aria-label="Illustrated ferns, leaves and orange flowers">
      <defs>
        <linearGradient id="foliage" x1="0" y1="0" x2="1" y2="1">
          <stop offset="0" stop-color="#2f8f3a"/>
          <stop offset="1" stop-color="#6cbf45"/>
        </linearGradient>
      </defs>
      <path d="M0 119 V30 C30 20 60 5 80 10 C110 0 130 30 150 60 C190 50 240 80 245 119 Z" fill="url(#foliage)"/>
    </svg>
  </section>

  <section class="panel panel--contact">
    <h2 class="heading" style="top:78px;">
      <span class="heading__lead">Who do</span>
      <span class="heading__main">I contact?</span>
    </h2>

    <svg class="scene" style="left:0; top:620px;" width="400" height="229" viewBox="0 0 400 229" role="img" aria-label="Silhouette of a hiker in a hat standing among bushes, with birds in the sky">
      <defs>
        <linearGradient id="bush" x1="0" y1="0" x2="0" y2="1">
          <stop offset="0" stop-color="#2f8a3c"/>
          <stop offset="1" stop-color="#0b4a2d"/>
        </linearGradient>
      </defs>
      <path d="M0 80 C40 70 80 110 130 100 C170 60 200 60 240 105 C290 95 340 60 400 90 V229 H0 Z" fill="url(#bush)"/>
    </svg>
  </section>

  <div class="portrait"><div class="portrait__photo" role="img" aria-label="Headshot photo of Diogenes Thessaly"></div></div>

  <h3 class="contact contact__name">Diogenes Thessaly</h3>
  <p class="contact contact__details">0452 318 947<br>diogenes.thessaly@example.com</p>
  <p class="contact contact__bio">Diogenes has a background in mental health support work, nature-connection mentoring, bush craft, outdoor leadership, group facilitation, youth work, and ecological restoration. He also has qualifications in psychology and ecology.</p>

  <section class="panel panel--cover">
    <svg class="scene" style="left:70px; top:138px;" width="320" height="90" viewBox="0 0 320 90" aria-label="Wildroot Support Services">
      <circle cx="18" cy="32" r="16" fill="var(--forest)"/>
      <text x="46" y="46" font-family="Roboto, sans-serif" font-weight="700" font-size="38" fill="var(--forest)">Wildroot</text>
      <text x="48" y="76" font-family="Roboto, sans-serif" font-weight="700" font-size="17" fill="var(--forest)" letter-spacing="0.3">SUPPORT SERVICES</text>
    </svg>

    <svg class="scene" style="left:0; top:252px;" width="400" height="597" viewBox="0 0 400 597" role="img" aria-label="Illustration of two campers toasting marshmallows by a campfire beside a lake, with pine trees, green hills and sky">
      <defs>
        <linearGradient id="landscape" x1="0" y1="0" x2="0" y2="1">
          <stop offset="0" stop-color="#9fd8f2"/>
          <stop offset="0.35" stop-color="#d8ecf6"/>
          <stop offset="0.55" stop-color="#7dbb44"/>
          <stop offset="0.72" stop-color="#1c6f63"/>
          <stop offset="1" stop-color="#0e3c5c"/>
        </linearGradient>
      </defs>
      <path d="M0 0 C40 90 110 110 160 110 C230 110 260 200 300 230 C340 240 370 230 400 220 V597 H0 Z" fill="url(#landscape)"/>
    </svg>
  </section>

</main>
</body>
</html>
```